KAY VELORE

We need a letterhead design for an Image & Etiquette Consultancy company based in Singapore.

The services we provide are Personal Image Consultation, Image & Etiquette Workshop for schools and corporate.

The design should have our corporate colour as seen in the logo files I have uploaded.

Since our company helps clients with their image, the design should be aesthetically very appealing. It should reflect a very classy & elegant feel.

I will print the letterhead using my printer but most of the time will use it to write letters to my clients therefore the format should include MS Word.

```html
<!DOCTYPE html>
<html lang="en">
<head>
<meta charset="utf-8">
<title>Kay Velore Letterhead</title>
<link href="https://fonts.googleapis.com/css2?family=Questrial&display=swap" rel="stylesheet">
<style>
  :root {
    --backdrop: #c9c4cb;
    --paper: #f2f2f2;
    --ink: #3a3a3c;
    --purple: #3b2346;
    --gold: #e8b51a;
    --silver: #b9b9bc;
  }
  * { margin: 0; padding: 0; box-sizing: border-box; }
  html, body { width: 1200px; height: 1000px; overflow: hidden; }
  body {
    background: var(--backdrop);
    font-family: "Questrial", "Century Gothic", sans-serif;
    color: var(--ink);
    position: relative;
  }
  .letterhead {
    position: absolute;
    left: 290px; top: 63px;
    width: 622px; height: 880px;
    background: var(--paper);
    overflow: hidden;
  }
  .brand {
    position: absolute; left: 58px; top: 58px;
    display: flex; align-items: center; gap: 8px;
  }
  .brand-mark { width: 10px; height: 10px; background: var(--gold); }
  .brand-name {
    font-size: 29px; letter-spacing: 1px; color: var(--purple); line-height: 1;
  }
  .contact {
    position: absolute; left: 467px; top: 60px;
    font-size: 8.5px; line-height: 12.5px;
  }
  .contact-item { display: flex; align-items: center; gap: 6px; }
  .contact-item svg { width: 9px; height: 9px; flex: none; }
  .contact-address { margin-top: 5px; }
  .date { position: absolute; left: 58px; top: 146px; font-size: 9.5px; }
  .recipient {
    position: absolute; left: 58px; top: 169px;
    font-size: 9.5px; line-height: 11.5px; font-style: normal;
  }
  .fold-mark { position: absolute; left: 0; width: 28px; height: 1px; background: #d4d4d6; }
  .fold-mark.upper { top: 313px; }
  .fold-mark.lower { top: 623px; }
  .salutation { position: absolute; left: 58px; top: 283px; font-size: 9.5px; font-weight: 700; }
  .body-copy {
    position: absolute; left: 58px; top: 317px; width: 506px;
    font-size: 9.6px; line-height: 11.2px; letter-spacing: 0.2px; text-align: justify;
  }
  .body-copy p { margin-bottom: 11px; }
  .closing { position: absolute; left: 58px; top: 564px; font-size: 9.5px; line-height: 12px; }
  .closing strong { display: block; }
  .signature-area {
    position: absolute; left: 134px; top: 556px; width: 128px; height: 62px;
    background: linear-gradient(120deg, rgba(116,130,198,0.18), rgba(116,130,198,0.32));
    border-radius: 4px;
  }
  .footer-band { position: absolute; left: 0; bottom: 0; width: 622px; }
  .footer-band .gold-rule { height: 3px; background: var(--gold); }
  .footer-band .silver-rule { height: 2px; margin-top: 3px; background: var(--silver); }
  .footer-band .purple-block { height: 26px; margin-top: 3px; background: var(--purple); }
</style>
</head>
<body>
  <main class="letterhead">
    <header>
      <div class="brand">
        <span class="brand-mark"></span>
        <span class="brand-name">KAY VELORE</span>
      </div>
      <div class="contact">
        <div class="contact-item">
          <svg viewBox="0 0 10 10"><rect width="10" height="10" rx="2" fill="var(--purple)"/><path d="M3 2.5 L4.2 2.5 L4.6 4 L3.9 4.6 Q4.6 6 5.6 6.3 L6.1 5.6 L7.5 6 L7.5 7.3 Q4.5 7.6 2.6 3.6 Z" fill="#fff"/></svg>
          <span>+65-6210 4837</span>
        </div>
        <div class="contact-item">
          <svg viewBox="0 0 10 10"><rect width="10" height="10" rx="2" fill="var(--purple)"/><rect x="2.3" y="3" width="5.4" height="4" fill="none" stroke="#fff" stroke-width="0.8"/><path d="M2.3 3 L5 5.2 L7.7 3" fill="none" stroke="#fff" stroke-width="0.8"/></svg>
          <span>hello@kayvelore.com</span>
        </div>
        <div class="contact-item">
          <svg viewBox="0 0 10 10"><rect width="10" height="10" rx="2" fill="var(--purple)"/><circle cx="5" cy="5" r="2.7" fill="none" stroke="#fff" stroke-width="0.7"/><path d="M2.3 5 H7.7 M5 2.3 Q3.6 5 5 7.7 M5 2.3 Q6.4 5 5 7.7" fill="none" stroke="#fff" stroke-width="0.6"/></svg>
          <span>www.kayvelore.com</span>
        </div>
        <div class="contact-address">18 Harbour Crest Road<br>Singapore 419302</div>
      </div>
    </header>

    <div class="date">30.02.2015</div>
    <address class="recipient">Recipient’s name<br>Lindenweg 4<br>10115 Berlin<br>Germany</address>

    <span class="fold-mark upper"></span>
    <span class="fold-mark lower"></span>

    <div class="salutation">Dear sir,</div>
    <section class="body-copy">
      <p>Communication is a very integral part of living creatures, animals and humans. Communication may be verbal or written. Written communication however is only applicable to human beings. Can you even imagine a world without communication? Verbal communication can be through telephones, webcams or in person. Written communication is through letters, emails and mobile phone messages.</p>
      <p>In today’s world of great inventions and technology, letters have somehow become redundant. It is the time for text messages or chats. But they still can communicate a lot more than all other modes of communication. Organizations and various government departments still bank on letters as a strong medium of communication. There is no comparison in costs of sending letters as compared to costs of mobile phone messages though – letters are far cheaper. Letters now commonly known as “hard copy documents” are considered more relevant and important than email copies of text messages as proof or evidence of some sort.</p>
      <p>Letters speak volumes about a person or an organization that writes it. So one must take utmost care ensuring that the language used in any letter is appropriate for the occasion for which it is being written. Since a letter is also a written proof or document, if there are certain things that should not form a part of it, then that too should be carefully handled.</p>
      <p>Writing a good letter is an art. But if for some reason someone is unable to write that perfect letter, these different types of letters provide a base for you to build on. Sample letters have been given for everyone to understand what all information needs to form a part of the letter type and then it can be customized.</p>
    </section>

    <div class="closing">Yours Sincerely,<strong>Elin Marsh</strong></div>
    <div class="signature-area" role="img" aria-label="Handwritten signature"></div>

    <footer class="footer-band" aria-hidden="true">
      <div class="gold-rule"></div>
      <div class="silver-rule"></div>
      <div class="purple-block"></div>
    </footer>
  </main>
</body>
</html>
```